Chinese Herbal and Roots Shop design

Hello Designers,

We are a herbal startup company which sells Chinese Herbal Products. we are looking for a responsive and unqiue Ecommerce web design.
Our business name is velorin and our area of business cut across the entire United States.

We don't have a logo at the moment and designers who come up with a great logo is more likely to be awarded winner of the consent.

The design needs to be completely custom design and we are not after just a template design. Please be creative and at the same time design have to be professionally looking and easy to navigate.
A theme which suits a herbal products are desired. We are open to different colors excpet RED and PINK.

NAVIGATION
Header -
Home, products, offers, Blog, cart, login/account

Footer -
Please refer to other Ecommerce websites

Page requires:
HOME PAGE
1. slider(Highlist products)
2. FEATURE PRODUCTS
3. Latest products
4. Most selling products
5. Deal of the day
6. Email capture (Newsletter/signup)
7. Social media links
8. Footer

PRODUCT PAGE
All the products will be present here with required details (price, short note and offers if any)

PRODUCT DETAILS PAGE
A well designed detailed page for a particular product covers the details of the price, increment, short description, purchase and other add to cart button. A section with similar products should be listed below aswell.

Industry/Entity Type

It Company

Coding

Coded - Design and coding required

```html
<!DOCTYPE html>
<html lang="en">
<head>
<meta charset="utf-8">
<title>Velorin – Chinese Herbal and Roots Shop</title>
<link href="https://fonts.googleapis.com/css2?family=Open+Sans:wght@400;600;700&display=swap" rel="stylesheet">
<style>
:root{
  --green:#6ea50f;
  --green-dark:#5b8d06;
  --orange:#f7931e;
  --ink:#2b2b2b;
  --muted:#8a8a8a;
  --line:#dcdcdc;
  --paper:#ffffff;
  --hero-bg:#f3f3f3;
}
*{box-sizing:border-box;margin:0;padding:0}
html,body{width:1200px;height:2839px;overflow:hidden}
body{position:relative;background:var(--paper);font-family:"Open Sans",Arial,sans-serif;color:var(--ink)}
.abs{position:absolute}

/* top bar */
.topbar{left:0;top:0;width:1200px;height:48px;border-bottom:1px solid #eee}
.topbar .phone{left:100px;top:12px;font-size:18px;color:#555;display:flex;align-items:center;gap:6px}
.search{left:485px;top:9px;width:325px;height:29px;border:1px solid #ccc;display:flex}
.search span{flex:1;font-size:11px;color:#999;padding:7px 8px}
.search i{width:28px;background:#222;display:flex;align-items:center;justify-content:center}
.toplink{top:13px;font-size:16px;color:#777;display:flex;align-items:center;gap:8px}

/* header */
.header{left:0;top:48px;width:1200px;height:113px;border-bottom:1px solid #eee}
.brand{left:97px;top:32px;font-size:40px;font-weight:400;color:var(--green)}
.nav{top:50px;font-size:19px;color:#888}
.nav.active{color:var(--ink)}
.cart{left:941px;top:37px;width:163px;height:48px;border-radius:24px;background:var(--orange);color:#fff;font-size:17px;font-weight:600;display:flex;align-items:center;justify-content:center;gap:8px}
.cart small{font-weight:400;font-size:15px;opacity:.85}

/* hero */
.hero{left:0;top:161px;width:1200px;height:500px;background:var(--hero-bg);overflow:hidden}
.hero-photo{left:470px;top:0;width:730px;height:500px;background:radial-gradient(ellipse at 45% 45%,#c79a6a 0,#e9d6c4 28%,#f6ece4 48%,var(--hero-bg) 70%)}
.hero h1{left:108px;top:150px;font-size:44px;font-weight:600;line-height:50px;color:#222}
.hero h1 em{font-style:normal;color:var(--orange)}
.btn-shop{left:112px;top:271px;width:136px;height:38px;background:var(--green);color:#fff;font-size:14px;font-weight:600;display:flex;align-items:center;justify-content:center}
.dots{left:114px;top:337px;display:flex;gap:6px}
.dots b{width:12px;height:12px;border-radius:50%;background:#777}
.dots b:first-child{background:none;border:2px solid #777}
.wave{left:0;top:560px;width:1200px;height:110px}

/* section titles */
.sec-title{left:0;width:1200px;text-align:center;font-size:25px;display:flex;justify-content:center;align-items:center;gap:14px}
.sec-title .rule{width:60px;height:2px;position:relative}
.sec-title .rule::after{content:"";position:absolute;top:-3px;width:8px;height:8px;border-radius:50%;background:inherit}
.rule.l::after{right:0}.rule.r::after{left:0}

/* product cards */
.card{background:#fff;border:1px solid var(--line)}
.card .img{position:absolute;left:14px;right:14px;top:14px;border-radius:2px}
.card .title{position:absolute;left:28px;font-size:20px;color:#222}
.card .desc{position:absolute;left:28px;font-size:13px;color:var(--muted);white-space:nowrap}
.card .price{position:absolute;left:28px;font-size:22px;color:var(--orange)}
.card .buy{position:absolute;right:22px;width:100px;height:30px;border:2px solid var(--green);border-radius:16px;font-size:13px;font-weight:700;color:#333;display:flex;align-items:center;justify-content:center}
.feat .img{height:200px}
.feat .title{top:236px}.feat .desc{top:268px}.feat .price{top:304px}.feat .buy{top:304px}
.small .img{left:0;right:0;top:0;height:205px}
.small .title{top:230px;left:26px;font-size:19px}.small .desc{top:262px;left:26px;font-size:12px}
.small .price{top:289px;left:26px;font-size:21px}.small .buy{top:288px;right:18px;width:98px}

.band{left:0;top:1183px;width:1200px;height:502px;background:linear-gradient(90deg,#a86348 0,#e4d9c9 14%,#efe7dc 50%,#e6dccf 86%,#7e4c3c 100%)}

/* deal & newsletter */
.deal{left:104px;top:2203px;width:488px;height:188px;display:flex;overflow:hidden}
.deal-copy{width:230px;background:var(--orange);color:#fff;padding:20px 0 0 24px;position:relative}
.deal-copy h3{font-size:27px;line-height:29px;font-weight:700}
.deal-copy p{font-size:10px;line-height:13px;margin-top:8px;width:158px;opacity:.85}
.deal-copy .click{position:absolute;left:24px;top:140px;width:120px;height:30px;border:2px solid #fff;font-size:13px;display:flex;align-items:center;justify-content:center}
.badge{position:absolute;left:190px;top:40px;width:72px;height:72px;border-radius:50%;background:#fff;color:var(--orange);font-size:15px;font-weight:700;line-height:16px;display:flex;align-items:center;justify-content:center;text-align:center;z-index:2}
.deal-photo{flex:1;background:linear-gradient(180deg,#8a6d52 0,#c9a679 45%,#d7b684 70%,#c9a227 100%)}
.news{left:611px;top:2205px;width:474px;height:184px;background:#f2f2f2;border:2px solid #ddd;padding:30px 0 0 32px}
.news h3{font-size:24px;font-weight:400;color:#222}
.news .field{margin-top:14px;width:414px;height:34px;background:#fff;border:1px solid #ddd;font-size:12px;color:#999;display:flex;align-items:center;gap:8px;padding-left:10px}
.news .sub{margin-top:10px;width:138px;height:40px;background:var(--green);color:#fff;font-size:18px;font-weight:600;display:flex;align-items:center;justify-content:center}

/* footer */
.footer{left:0;top:2440px;width:1200px;height:399px}
.fcol{top:2548px;color:#fff}
.fcol h4{font-size:18px;font-weight:400;margin-bottom:20px}
.fcol li{list-style:none;font-size:13px;line-height:30px;color:#e8f2d6}
.socials{display:flex;gap:12px;margin-top:4px}
.socials b{width:36px;height:36px;border-radius:50%;background:#fff;opacity:.9}
.cards{display:flex;gap:8px;margin-top:18px}
.cards b{width:36px;height:22px;border-radius:3px;background:#fff}
.frule{left:80px;top:2764px;width:1040px;height:1px;background:rgba(255,255,255,.35)}
.copy{left:0;top:2786px;width:1200px;text-align:center;font-size:13px;color:#e1eecb}
</style>
</head>
<body>

<div class="abs topbar">
  <div class="abs phone"><svg width="18" height="18" viewBox="0 0 24 24"><path fill="#555" d="M6.6 10.8a15 15 0 0 0 6.6 6.6l2.2-2.2c.3-.3.7-.4 1-.2 1.1.4 2.3.6 3.6.6.6 0 1 .4 1 1V20c0 .6-.4 1-1 1A17 17 0 0 1 3 4c0-.6.4-1 1-1h3.5c.6 0 1 .4 1 1 0 1.3.2 2.5.6 3.6.1.3 0 .7-.2 1z"/></svg>(555) 214-0387</div>
  <div class="abs search"><span>Enter Keyword</span><i><svg width="13" height="13" viewBox="0 0 24 24"><circle cx="10" cy="10" r="7" stroke="#fff" stroke-width="3" fill="none"/><path d="M15 15l6 6" stroke="#fff" stroke-width="3"/></svg></i></div>
  <div class="abs toplink" style="left:909px"><svg width="20" height="18" viewBox="0 0 24 22"><rect x="2" y="4" width="16" height="16" fill="none" stroke="#999" stroke-width="2"/><path d="M9 13l11-11 2 2-11 11H9z" fill="#999"/></svg>Login</div>
  <div class="abs toplink" style="left:1003px"><svg width="18" height="18" viewBox="0 0 24 24"><circle cx="12" cy="7" r="5" fill="#aaa"/><path d="M2 23c0-6 4-9 10-9s10 3 10 9z" fill="#aaa"/></svg>Account</div>
</div>

<header class="abs header">
  <div class="abs brand">Velorin</div>
  <div class="abs nav active" style="left:526px">Home</div>
  <div class="abs nav" style="left:627px">Products</div>
  <div class="abs nav" style="left:750px">Offers</div>
  <div class="abs nav" style="left:852px">Blog</div>
  <div class="abs cart"><svg width="24" height="20" viewBox="0 0 24 20"><path d="M1 6h22l-3 13H4z" fill="none" stroke="#fff" stroke-width="2"/><path d="M7 6l4-5M17 6l-4-5" stroke="#fff" stroke-width="2"/></svg>Cart <small>0 Items</small></div>
</header>

<section class="abs hero">
  <div class="abs hero-photo" role="img" aria-label="Open hands holding a mix of dried Chinese herbs and roots"></div>
  <h1 class="abs">Chinese Herbal and<br><em>Roots Shop</em></h1>
  <div class="abs btn-shop">SHOP NOW</div>
  <div class="abs dots"><b></b><b></b><b></b><b></b></div>
</section>
<svg class="abs wave" viewBox="0 0 1200 110" preserveAspectRatio="none"><path d="M0 60 C300 130 700 20 1200 60 L1200 110 L0 110Z" fill="#fff"/><path d="M0 60 C300 130 700 20 1200 60" fill="none" stroke="#ddd" stroke-width="2"/></svg>

<div class="abs sec-title" style="top:708px;color:var(--orange)"><i class="rule l" style="background:var(--orange)"></i>Feature Products<i class="rule r" style="background:var(--orange)"></i></div>

<div class="abs card feat" style="left:100px;top:767px;width:326px;height:342px"><div class="img" role="img" aria-label="Lavender, oil bottles and herbal soap" style="background:linear-gradient(135deg,#f6f3f6,#b3a0c6 50%,#8b6a4d 80%,#f7f5f7)"></div><div class="title">Product Tittle</div><div class="desc">Maecenas at justo id velit placerat moles</div><div class="price">$25.99</div><div class="buy">Buy Now</div></div>
<div class="abs card feat" style="left:439px;top:767px;width:326px;height:342px"><div class="img" role="img" aria-label="Glass jar of herbal cream with sprigs" style="background:linear-gradient(135deg,#f7f9f7,#cfe4e8 45%,#9bb67c 75%,#f7f7f7)"></div><div class="title">Product Tittle</div><div class="desc">Maecenas at justo id velit placerat moles</div><div class="price">$25.99</div><div class="buy">Buy Now</div></div>
<div class="abs card feat" style="left:780px;top:767px;width:326px;height:342px"><div class="img" role="img" aria-label="Bundle of dried roots" style="background:linear-gradient(135deg,#f8f8f6,#7a5a3b 50%,#5f6a3a 70%,#f8f8f6)"></div><div class="title">Product Tittle</div><div class="desc">Maecenas at justo id velit placerat moles</div><div class="price">$25.99</div><div class="buy">Buy Now</div></div>

<div class="abs band" role="img" aria-label="Wooden table with dried berries, spices and herbs"></div>
<div class="abs sec-title" style="top:1226px;color:#222"><i class="rule l" style="background:var(--green)"></i>Latest Products<i class="rule r" style="background:var(--green)"></i></div>

<div class="abs card small" style="left:100px;top:1285px;width:244px;height:343px"><div class="img" role="img" aria-label="Herbal tea cup with dried slices" style="background:linear-gradient(135deg,#fbfaf4,#e8d25a 45%,#8b5a2b 75%,#fbfaf4)"></div><div class="title">Product Tittle</div><div class="desc">sociosqu ad litora torquent per</div><div class="price">$25.99</div><div class="buy">Buy Now</div></div>
<div class="abs card small" style="left:356px;top:1285px;width:244px;height:343px"><div class="img" role="img" aria-label="Lavender oils and soap bars" style="background:linear-gradient(135deg,#f6f3f6,#b3a0c6 50%,#8b6a4d 80%,#f7f5f7)"></div><div class="title">Product Tittle</div><div class="desc">sociosqu ad litora torquent per</div><div class="price">$25.99</div><div class="buy">Buy Now</div></div>
<div class="abs card small" style="left:611px;top:1285px;width:244px;height:343px"><div class="img" role="img" aria-label="Heap of loose black tea leaves" style="background:radial-gradient(circle at 50% 45%,#2a2a2a 0,#4a4a4a 35%,#f4f4f4 70%)"></div><div class="title">Product Tittle</div><div class="desc">sociosqu ad litora torquent per</div><div class="price">$25.99</div><div class="buy">Buy Now</div></div>
<div class="abs card small" style="left:865px;top:1285px;width:244px;height:343px"><div class="img" role="img" aria-label="Clay tea pot with green tea leaves" style="background:linear-gradient(135deg,#fafaf7,#7a4a2a 45%,#8e9a5a 75%,#fafaf7)"></div><div class="title">Product Tittle</div><div class="desc">sociosqu ad litora torquent per</div><div class="price">$25.99</div><div class="buy">Buy Now</div></div>

<div class="abs sec-title" style="top:1724px;color:#222"><i class="rule l" style="background:var(--green)"></i>Most Selling<i class="rule r" style="background:var(--green)"></i></div>

<div class="abs card small" style="left:100px;top:1783px;width:244px;height:343px"><div class="img" role="img" aria-label="Spray bottle with lavender bunch" style="background:linear-gradient(180deg,#fff,#9a5a2a 40%,#9a86c4 70%,#fff)"></div><div class="title">Product Tittle</div><div class="desc">sociosqu ad litora torquent per</div><div class="price">$25.99</div><div class="buy">Buy Now</div></div>
<div class="abs card small" style="left:356px;top:1783px;width:244px;height:343px"><div class="img" role="img" aria-label="Cream jar with fresh basil leaves" style="background:radial-gradient(circle at 50% 55%,#5ea03a 0,#9cc97a 30%,#fff 65%)"></div><div class="title">Product Tittle</div><div class="desc">sociosqu ad litora torquent per</div><div class="price">$25.99</div><div class="buy">Buy Now</div></div>
<div class="abs card small" style="left:611px;top:1783px;width:244px;height:343px"><div class="img" role="img" aria-label="Massage oil, flowers and spa stones" style="background:linear-gradient(135deg,#fff,#e0a23a 40%,#3a3a3a 70%,#fff)"></div><div class="title">Product Tittle</div><div class="desc">sociosqu ad litora torquent per</div><div class="price">$25.99</div><div class="buy">Buy Now</div></div>
<div class="abs card small" style="left:865px;top:1783px;width:244px;height:343px"><div class="img" role="img" aria-label="Handmade yellow soap bars" style="background:radial-gradient(circle at 50% 50%,#f3d27a 0,#f7e6b0 35%,#fff 65%)"></div><div class="title">Product Tittle</div><div class="desc">sociosqu ad litora torquent per</div><div class="price">$25.99</div><div class="buy">Buy Now</div></div>

<div class="abs deal">
  <div class="deal-copy"><h3>DEAL OF<br>THE DAY</h3><p>Save on hand-picked roots and dried herbs today only</p><div class="click">CLICK HERE</div></div>
  <div class="badge">15%<br>OFF</div>
  <div class="deal-photo" role="img" aria-label="Market crates of dried ginseng roots"></div>
</div>

<div class="abs news">
  <h3>JOIN NEWSLETTERS</h3>
  <div class="field"><svg width="14" height="11" viewBox="0 0 14 11"><rect x=".5" y=".5" width="13" height="10" fill="none" stroke="#999"/><path d="M.5.5l6.5 5 6.5-5" fill="none" stroke="#999"/></svg>Email address</div>
  <div class="sub">Subscribe</div>
</div>

<svg class="abs footer" viewBox="0 0 1200 399" preserveAspectRatio="none"><path d="M0 30 C200 -10 420 50 700 20 C900 0 1050 40 1200 20 L1200 399 L0 399Z" fill="var(--green)"/></svg>

<div class="abs fcol" style="left:97px"><h4>MY ACCOUNT</h4><ul><li>Privacy Policy</li><li>Your Account</li><li>Advanced Search</li><li>Contact Us</li></ul></div>
<div class="abs fcol" style="left:293px"><h4>COMPANY</h4><ul><li>Contact us</li><li>About us</li><li>Privacy</li><li>FAQs</li></ul></div>
<div class="abs fcol" style="left:458px"><h4>RESOURCES</h4><ul><li>About us</li><li>Blog</li><li>Company</li><li>Support</li></ul></div>
<div class="abs fcol" style="left:640px"><h4>CONTACT US</h4><ul><li style="line-height:22px">48 Willow Bend Road Suite 12<br>Fairhaven, OR 97321</li><li style="margin-top:14px;line-height:22px">(555) 214-0387<br>hello@velorinherbs.com</li></ul></div>
<div class="abs fcol" style="left:875px"><h4>STAY IN TOUCH</h4><div class="socials"><b></b><b></b><b></b><b></b><b></b></div><div class="cards"><b></b><b></b><b></b><b></b><b></b></div></div>

<div class="abs frule"></div>
<div class="abs copy">© 2017 Company Name. All right reserved. Term of Use</div>

</body>
</html>
```